Maple Hollow Ranch Business Card

Farm selling Nigerian Dwarf Goats, Bison, chickens, and miniature donkeys. Additionally we sell goats milk, goats milk soap and goat cheese, bison meat, bison heads, and bison skins, and chicken eggs.
Address 4127 Thornbury Lane
Hopkinsville, KY 42240
Phone number 615-382-9154
Website: MapleHollowRanch@ridgemail.net
I will upload my farm logo, cheese label, and soap label to give you ideas of my theme.
I want a really catchy card that people will remember.

```html
<!DOCTYPE html>
<html lang="en">
<head>
<meta charset="UTF-8">
<title>Maple Hollow Ranch Business Card</title>
<link rel="stylesheet" href="https://fonts.googleapis.com/css2?family=Oswald:wght@500&family=Exo+2:wght@400;600&display=swap">
<style>
  :root {
    --backdrop: #2b2b2d;
    --card-brown: #2e2723;
    --band-grey: #3d3936;
    --gold: #e6a716;
    --amber: #d9860f;
    --beige: #c9b49c;
    --white: #ffffff;
    --text-light: #f2eee9;
  }
  * { margin: 0; padding: 0; box-sizing: border-box; }
  html, body { width: 1200px; height: 820px; overflow: hidden; }
  body { background: var(--backdrop); position: relative; font-family: "Exo 2", sans-serif; }

  .card { position: absolute; top: 255px; width: 540px; height: 310px; overflow: hidden; }
  .card-front { left: 50px; background: var(--card-brown); }
  .card-back { left: 610px; }
  .card svg.card-art { position: absolute; inset: 0; width: 100%; height: 100%; }

  .brand { position: absolute; left: 40px; top: 40px; display: flex; align-items: center; gap: 18px; }
  .brand-circle { width: 78px; height: 78px; border-radius: 50%; border: 3px solid var(--gold); flex: none; }
  .brand-name { font-family: "Oswald", sans-serif; font-weight: 500; color: var(--gold); font-size: 30px; letter-spacing: 2px; text-transform: uppercase; white-space: nowrap; }

  .contact { position: absolute; left: 40px; top: 142px; color: var(--text-light); font-size: 12.5px; line-height: 22px; }
  .contact-item { display: flex; align-items: center; gap: 7px; white-space: nowrap; }
  .contact-item svg { width: 12px; height: 12px; fill: var(--text-light); flex: none; }

  .name-band { position: absolute; left: 0; bottom: 0; width: 100%; height: 78px; display: flex; align-items: center; }
  .person-name { position: relative; margin-left: 40px; font-family: "Oswald", sans-serif; font-weight: 500; color: var(--white); font-size: 30px; letter-spacing: 1.5px; text-transform: uppercase; white-space: nowrap; }
  .divider { position: relative; width: 4px; height: 48px; background: var(--amber); margin: 0 22px; transform: skewX(-18deg); }
  .person-title { position: relative; color: var(--text-light); font-size: 14px; letter-spacing: 2px; text-transform: uppercase; white-space: nowrap; }
</style>
</head>
<body>

<section class="card card-front">
  <svg class="card-art" viewBox="0 0 540 310" aria-hidden="true">
    <polygon points="0,232 540,232 540,310 0,310" fill="var(--band-grey)"/>
    <polygon points="470,0 540,0 540,60" fill="var(--gold)"/>
    <polygon points="0,250 0,310 40,310" fill="var(--gold)"/>
  </svg>

  <div class="brand">
    <div class="brand-circle"></div>
    <div class="brand-name">Maple Hollow Ranch</div>
  </div>

  <div class="contact">
    <div class="contact-item">
      <svg viewBox="0 0 12 12"><path d="M6 0.5a4 4 0 0 1 4 4c0 3-4 7-4 7s-4-4-4-7a4 4 0 0 1 4-4zm0 2.5a1.5 1.5 0 1 0 0 3a1.5 1.5 0 0 0 0-3z"/></svg>4127 Thornbury Lane, Hopkinsville, KY 42240
    </div>
    <div class="contact-item">
      <svg viewBox="0 0 12 12"><path d="M2 1h3l1 3-2 1a7 7 0 0 0 3 3l1-2 3 1v3a1 1 0 0 1-1 1A10 10 0 0 1 1 2a1 1 0 0 1 1-1z"/></svg>615-382-9154
    </div>
    <div class="contact-item">
      <svg viewBox="0 0 12 12"><path d="M1 3h10v7H1zM1 3l5 4 5-4" stroke="var(--card-brown)" stroke-width="0.8"/></svg>MapleHollowRanch@ridgemail.net
    </div>
  </div>

  <div class="name-band">
    <span class="person-name">Daniel Whitcomb</span>
    <span class="divider"></span>
    <span class="person-title">Farm Owner</span>
  </div>
</section>

<section class="card card-back">
  <svg class="card-art" viewBox="0 0 540 310" aria-hidden="true">
    <rect width="540" height="310" fill="var(--gold)"/>
    <polygon points="60,0 170,0 20,310 -90,310" fill="var(--beige)"/>
    <polygon points="178,0 186,0 36,310 28,310" fill="var(--white)"/>
    <polygon points="270,0 300,0 150,310 120,310" fill="var(--card-brown)"/>
    <polygon points="300,0 420,0 270,310 150,310" fill="var(--gold)"/>
    <polygon points="428,0 436,0 286,310 278,310" fill="var(--white)"/>
    <polygon points="450,0 560,0 410,310 300,310" fill="var(--beige)"/>
    <polygon points="560,0 568,0 418,310 410,310" fill="var(--white)"/>
  </svg>
</section>

</body>
</html>
```